Corvanel Hand Sanitizer - Label Design

hand sanitizer label -the brand is Corvanel, I'm looking to make a hand sanitizer label that will look nice and clean not too fancy with design that when you look at it you think about: clean healthy, germ free, I would like to do it with transparent background design that will look good in greenish color (with aloe) and or blueish color (refreshing scent) maybe even yellowish color(with lemon scent) only one main
color not together
Bottle size: 8oz (see attach)
Label size: 3 inches Height , 5 inches Width (see attach)
Target Market(s)
all people all ages
Industry/Entity Type
Health Product
Font styles to use
Requirements
Must have
- 1. label size is 3 inches Height , 5 inches Width Please see attach
2. to add Drog facts on the label
3. on the bottom of the frog facts change to Manufacture For:
4. one version for lemon version and one for Aloe version
Corvanel 4817 W Halberd Ave Las Vegas NV 89146
- will need to have the words: hand sanitizer
- will need to look good as blueish color and or greenish color
- play with the name Corvanel in attractive way maybe larger X or Corvanel or something like that
- the words: kill 99.9% germs
- the words: 70% alcohol
- the words: corvanelus.example (very small letters on the bottom of the label)
- the words: vitamin E & aloe
- the words: 8oz ( 236mil )on the lower area of the label
*transparent label
Nice to have
- - a small carton of sick germ or scared germ (see example on the attach)
- of maybe on the side some clean bubbles or something that will give clean feeling
- maybe aloe leaf
Should not have
- it should not have childish look
open for ideas

```html
<!DOCTYPE html>
<html lang="en">
<head>
<meta charset="utf-8">
<title>Corvanel Hand Sanitizer Label</title>
<link rel="stylesheet" href="https://fonts.googleapis.com/css2?family=Roboto+Slab:wght@800&family=Barlow:wght@600&display=swap">
<style>
  :root {
    --sky: #56b7e6;
    --leaf: #7cc142;
    --paper: #ffffff;
    --stage: #ececec;
    --germ-green: #7cc142;
    --germ-red: #e42f2c;
  }
  * { margin: 0; padding: 0; box-sizing: border-box; }
  html, body {
    width: 1121px;
    height: 1200px;
    overflow: hidden;
    background: var(--stage);
  }
  .label {
    position: absolute;
    left: 12px;
    top: 0;
    width: 1097px;
    height: 1200px;
    background: var(--paper);
    overflow: hidden;
  }
  .brand-name {
    position: absolute;
    left: 0;
    right: 0;
    top: 196px;
    text-align: center;
    font-family: "Barlow", sans-serif;
    font-weight: 600;
    font-size: 150px;
    line-height: 1;
    color: var(--sky);
  }
  .product-type {
    position: absolute;
    left: 0;
    right: 0;
    top: 386px;
    text-align: center;
    font-family: "Roboto Slab", serif;
    font-weight: 800;
    font-size: 58px;
    line-height: 1;
    color: var(--sky);
  }
  .claims-band {
    position: absolute;
    left: 0;
    top: 623px;
    width: 800px;
    height: 248px;
    background: var(--sky);
  }
  .badge-cutout {
    position: absolute;
    left: 699px;
    top: 561px;
    width: 332px;
    height: 332px;
    border-radius: 50%;
    background: var(--paper);
  }
  .germ-illustration {
    position: absolute;
    left: 712px;
    top: 574px;
    width: 306px;
    height: 306px;
    border-radius: 50%;
    background: radial-gradient(circle closest-side, var(--germ-green) 0%, var(--germ-green) 84%, var(--germ-red) 86%, var(--germ-red) 100%);
  }
  .claims {
    position: absolute;
    left: 153px;
    top: 640px;
    list-style: none;
  }
  .claim {
    display: flex;
    align-items: center;
    height: 71px;
    font-family: "Barlow", sans-serif;
    font-weight: 600;
    font-size: 50px;
    color: var(--paper);
  }
  .claim-tick {
    width: 56px;
    height: 56px;
    margin-right: 20px;
    flex: none;
  }
  .net-volume,
  .website {
    position: absolute;
    left: 0;
    right: 0;
    text-align: center;
    font-family: "Barlow", sans-serif;
    font-weight: 600;
    font-size: 44px;
    line-height: 1;
    color: var(--leaf);
  }
  .net-volume { top: 988px; }
  .website { top: 1050px; }
</style>
</head>
<body>
  <div class="label">
    <h1 class="brand-name">Corvanel</h1>
    <h2 class="product-type">HAND SANITIZER</h2>

    <div class="claims-band"></div>
    <div class="badge-cutout"></div>
    <div class="germ-illustration" role="img" aria-label="Cartoon green germs inside a red no-entry sign"></div>

    <ul class="claims">
      <li class="claim">
        <svg class="claim-tick" viewBox="0 0 56 56" aria-hidden="true"><circle cx="28" cy="28" r="24" fill="none" stroke="#fff" stroke-width="5"/><path d="M17 29l8 8 14-16" fill="none" stroke="#fff" stroke-width="5" stroke-linecap="round" stroke-linejoin="round"/></svg>
        KILL 99.9% GERMS
      </li>
      <li class="claim">
        <svg class="claim-tick" viewBox="0 0 56 56" aria-hidden="true"><circle cx="28" cy="28" r="24" fill="none" stroke="#fff" stroke-width="5"/><path d="M17 29l8 8 14-16" fill="none" stroke="#fff" stroke-width="5" stroke-linecap="round" stroke-linejoin="round"/></svg>
        70% ALCOHOL
      </li>
      <li class="claim">
        <svg class="claim-tick" viewBox="0 0 56 56" aria-hidden="true"><circle cx="28" cy="28" r="24" fill="none" stroke="#fff" stroke-width="5"/><path d="M17 29l8 8 14-16" fill="none" stroke="#fff" stroke-width="5" stroke-linecap="round" stroke-linejoin="round"/></svg>
        vitamin E &amp; aloe
      </li>
    </ul>

    <p class="net-volume">8oz ( 236mil )</p>
    <p class="website">corvanelus.example</p>
  </div>
</body>
</html>
```